Pelbrook Business Cards

Create new business cards with the details below.

Aaron Velst
Director

MB: +61 412 563 904
PH: 1300 417 639
Email: aaron.velst@pelbrook.com.au
Address: 27C Marlow Parade, Thornvale VIC 3094 Australia
Website: www.pelbrook.com.au

Target Market(s)

Other business

Industry/Entity Type

Business

Requirements
Must have
• must be clean looking

```html
<!DOCTYPE html>
<html lang="en">
<head>
<meta charset="utf-8">
<title>Pelbrook Business Cards</title>
<link rel="stylesheet" href="https://fonts.googleapis.com/css2?family=Montserrat:wght@400;500;700&display=swap">
<style>
  :root {
    --stage: #202020;
    --paper: #ffffff;
    --lime: #a8cf38;
    --charcoal: #2b2b2b;
    --ink: #1e1e1e;
    --rule: #333333;
  }
  * { margin: 0; padding: 0; box-sizing: border-box; }
  html, body {
    width: 1200px; height: 1000px; overflow: hidden;
    background: var(--stage);
    font-family: "Montserrat", Arial, sans-serif;
  }
  .card {
    position: absolute; left: 250px;
    width: 700px; height: 400px;
    background: var(--paper);
    border-radius: 34px;
    overflow: hidden;
    box-shadow: 0 10px 30px rgba(0,0,0,.45);
  }
  .card-back { top: 70px; }
  .card-front { top: 530px; }
  .card svg.shapes { position: absolute; inset: 0; }
  .brand {
    position: absolute;
    display: flex; align-items: center; gap: 12px;
  }
  .brand-mark { width: 30px; height: 30px; background: var(--charcoal); }
  .brand-name {
    font-weight: 700; color: var(--lime);
    text-transform: uppercase; letter-spacing: 1px;
  }
  .card-back .brand { left: 40px; top: 72px; }
  .card-back .brand-name { font-size: 34px; }
  .card-front .brand { left: 0; right: 0; top: 150px; justify-content: center; }
  .card-front .brand-name { font-size: 46px; }
  .card-front .brand-mark { width: 40px; height: 40px; }
  .website {
    position: absolute; left: 0; right: 0; top: 215px;
    text-align: center; font-size: 20px; color: var(--ink); letter-spacing: .5px;
  }
  .person { position: absolute; right: 400px; top: 170px; text-align: right; }
  .person-name { font-size: 34px; font-weight: 400; color: var(--ink); }
  .person-role { font-size: 20px; color: var(--lime); margin-top: 2px; }
  .person-email { font-size: 13px; color: var(--ink); margin-top: 6px; }
  .contact {
    position: absolute; left: 460px; top: 70px;
    font-size: 14px; line-height: 1.45; color: var(--ink);
  }
  .contact .address { margin-top: 18px; }
</style>
</head>
<body>

<section class="card card-back" aria-label="Business card, back">
  <svg class="shapes" width="700" height="400" viewBox="0 0 700 400" aria-hidden="true">
    <polygon points="215,400 300,300 385,400" fill="var(--charcoal)"/>
    <polygon points="420,40 640,40 700,110 700,400 330,400" fill="var(--lime)"/>
    <line x1="420" y1="40" x2="700" y2="40" stroke="var(--rule)" stroke-width="1.5"/>
    <line x1="0" y1="145" x2="380" y2="145" stroke="var(--rule)" stroke-width="1.5"/>
  </svg>
  <div class="brand"><span class="brand-mark"></span><span class="brand-name">Pelbrook</span></div>
  <div class="person">
    <div class="person-name">Aaron Velst</div>
    <div class="person-role">Director</div>
    <div class="person-email">aaron.velst@pelbrook.com.au</div>
  </div>
  <div class="contact">
    <div>MB:&nbsp; +61 412 563 904</div>
    <div>PH:&nbsp;&nbsp; 1300 417 639</div>
    <div class="address">27C Marlow Parade,<br>Thornvale VIC 3094<br>Australia</div>
  </div>
</section>

<section class="card card-front" aria-label="Business card, front">
  <svg class="shapes" width="700" height="400" viewBox="0 0 700 400" aria-hidden="true">
    <polygon points="230,0 460,0 360,100" fill="var(--lime)"/>
    <polygon points="360,400 450,280 590,400" fill="var(--charcoal)"/>
  </svg>
  <div class="brand"><span class="brand-mark"></span><span class="brand-name">Pelbrook</span></div>
  <div class="website">www.pelbrook.com.au</div>
</section>

</body>
</html>
```